Thermlio Energy Ratings Whole Home Energy Rating Flyer

Please create a flyer 8.5" x 11" that is 2-sided that goes hand and hand with my tri-fold flyer. The flyer will target prospective homeowners and real estate agents to purchase a whole home energy rating. I have attached further details.

Target Market(s)

Homeowners looking to remodel their homes, save on energy bills, purchase or sell a home.

Font styles to use
Serif
Sans Serif

Colors
3176b5
ffffff

Requirements
Must have
• Must be able to sell a whole home energy rating on its own!
Nice to have
• I would like to mimic the colors and background of my tri-fold flyer.
Should not have
• Should not be boring!

```html
<!DOCTYPE html>
<html lang="en">
<head>
<meta charset="utf-8">
<title>Thermlio Energy Ratings – Whole Home Energy Rating Flyer</title>
<link href="https://fonts.googleapis.com/css2?family=Open+Sans:ital,wght@0,400;0,600;0,700;0,800;1,400&display=swap" rel="stylesheet">
<style>
  :root{
    --brand-blue:#3176b5;
    --ink:#111;
    --text:#333;
    --paper:#fff;
    --backdrop:#e9e9ea;
  }
  html,body{margin:0;padding:0;width:1200px;height:1200px;overflow:hidden;background:var(--backdrop);}
  body{font-family:"Open Sans",Arial,sans-serif;color:var(--text);}
  .flyer{position:absolute;left:182px;top:30px;width:835px;height:1140px;background:var(--paper);overflow:hidden;box-shadow:0 4px 14px rgba(0,0,0,.18);}
  .flyer svg.decor{position:absolute;left:0;top:0;}
  .brand{position:absolute;left:62px;top:92px;text-align:right;}
  .brand-name{font-weight:800;font-size:40px;color:var(--ink);letter-spacing:1px;line-height:1;}
  .brand-sub{font-size:12px;color:var(--brand-blue);letter-spacing:1px;margin-top:2px;}
  .house-art{position:absolute;left:295px;top:160px;width:265px;height:320px;background:linear-gradient(160deg,#f4f4f4,#d9d9d9 70%,#bcbcbc);border-radius:6px;}
  .plan-art{position:absolute;left:520px;top:110px;width:315px;height:330px;background:linear-gradient(200deg,#ece7de,#f7f5f1 60%,rgba(255,255,255,0));}
  .badge{position:absolute;left:60px;top:217px;width:180px;height:180px;border-radius:50%;background:#000;border:8px solid var(--brand-blue);display:flex;align-items:center;justify-content:center;text-align:center;color:#fff;font-size:17px;font-weight:600;line-height:1.3;padding:0 14px;box-sizing:border-box;}
  .rating-scale{position:absolute;left:560px;top:258px;}
  .rating-scale .band{height:30px;margin-bottom:4px;display:flex;align-items:center;color:#fff;font-weight:700;font-size:17px;padding-left:6px;box-sizing:border-box;clip-path:polygon(0 0,calc(100% - 16px) 0,100% 50%,calc(100% - 16px) 100%,0 100%);}
  .rating-scale .band b{font-weight:400;font-size:24px;margin-right:12px;width:14px;}
  .intro{position:absolute;left:62px;top:528px;width:730px;font-size:15.5px;line-height:1.3;color:#333;margin:0;}
  .panel{position:absolute;border:2px solid var(--brand-blue);box-sizing:border-box;}
  .panel h2{margin:0;background:#000;color:#fff;font-size:14.5px;font-weight:600;padding:6px 12px;}
  .panel p{margin:8px 10px;font-size:9.6px;line-height:1.3;}
  .panel-what{left:50px;top:597px;width:315px;height:197px;}
  .panel-who{left:375px;top:597px;width:410px;height:300px;}
  .panel-who p{margin-bottom:12px;}
  .bar-blue{position:absolute;left:50px;top:810px;width:315px;height:44px;background:var(--brand-blue);color:#fff;font-weight:600;font-size:14.5px;display:flex;align-items:center;padding-left:12px;box-sizing:border-box;}
  .performs-text{position:absolute;left:62px;top:866px;width:290px;font-size:9.8px;line-height:1.3;margin:0;}
  .bar-black{position:absolute;left:50px;top:940px;width:315px;background:#000;color:#fff;font-size:10px;line-height:1.25;padding:3px 12px;box-sizing:border-box;}
  .checklist{position:absolute;top:982px;list-style:none;margin:0;padding:0;font-size:11px;line-height:1.36;color:#444;}
  .checklist li{position:relative;padding-left:16px;white-space:nowrap;}
  .checklist li::before{content:"";position:absolute;left:2px;top:3px;width:4px;height:8px;border:solid var(--brand-blue);border-width:0 2px 2px 0;transform:rotate(40deg);}
  .checklist-a{left:58px;}
  .checklist-b{left:262px;}
  .notes{position:absolute;left:388px;top:906px;width:405px;font-size:8.2px;line-height:1.3;color:#444;}
  .notes p{margin:0 0 6px;}
</style>
</head>
<body>
<main class="flyer">
  <div class="plan-art" role="img" aria-label="Faint architectural blueprint drawing"></div>
  <svg class="decor" width="835" height="1140" viewBox="0 0 835 1140" aria-hidden="true">
    <polygon points="8,378 562,52 835,210 835,262 562,100 300,270 320,320 60,360" fill="#3176b5"/>
    <polygon points="0,1128 622,1086 835,1108 835,1140 0,1140" fill="#3176b5"/>
  </svg>
  <div class="house-art" role="img" aria-label="Illustration of a small white house with solar panels on a green roof"></div>

  <div class="brand">
    <div class="brand-name">THERMLIO</div>
    <div class="brand-sub">ENERGY RATINGS</div>
  </div>

  <div class="badge">Every report is custom tailored to each unique home.</div>

  <div class="rating-scale" aria-label="Energy rating scale">
    <div class="band" style="width:92px;background:#2f9a3a"><b>A</b>=50</div>
    <div class="band" style="width:112px;background:#5db32f"><b>B</b>51-90</div>
    <div class="band" style="width:132px;background:#a7c928"><b>C</b>91-150</div>
    <div class="band" style="width:152px;background:#efd61c"><b>D</b>151-230</div>
    <div class="band" style="width:172px;background:#e8b711"><b>E</b>231-330</div>
    <div class="band" style="width:192px;background:#ef7c1d"><b>F</b>331-450</div>
    <div class="band" style="width:212px;background:#d9242a"><b>G</b>&gt;450</div>
  </div>

  <p class="intro">*Would you like to lower your monthly energy bill, enjoy a safer, more comfortable and durable home, and increase your homes appraisal value and sales appeal? Then keep reading, because that is what a lost cost, home energy rating can do for you...</p>

  <section class="panel panel-what">
    <h2>What is a Whole Home Energy Rating?</h2>
    <p>A Whole Home Energy Rating is a comprehensive evaluation of the efficiency of the entire home. You will receive a written report that includes a numeric score or "rating" of the home, plus recommendations for improvements that will reduce energy bills and make the home more comfortable. Each rating will receive an official California Home Energy Rating Certificate and home energy rating report with the California Energy Commission's (CEC) seal. The report will identify the most cost-effective and appropriate energy efficiency improvements needed to save you money and provide long lasting comfort.</p>
  </section>

  <section class="panel panel-who">
    <h2>Who needs a Whole Home Energy Rating?</h2>
    <p>Everyone! Whether you are buying or selling, or plan on staying in your home for one year or the rest of your life, each whole home energy rating is geared toward helping you save money, and is custom tailored to fit your unique needs. The whole home energy rating can be designed to fit any lifestyle or energy improvement budget, with a focal point on cost effectiveness and common sense.</p>
    <p>Buyers who choose to get a whole home energy rating can better decide which home will save them money through energy efficiency! They may also be entitled to federal tax credits, and borrow up to $40,000 for energy improvements through their mortgage.</p>
    <p>Sellers who have a CEC certificate showing their homes energy efficiency ultimately make their homes more valuable and often sell their homes faster than those without documentation.</p>
    <p>Before you remodel your home, make sure you have a HERS Rater conduct a Whole Home Energy Rating so you know exactly where to focus your money.</p>
  </section>

  <div class="bar-blue">Who performs the rating?</div>
  <p class="performs-text">A Home Energy Rating System (HERS) Rater, who is certified by the CEC will conduct the rating. Each California HERS Rater must follow standardized energy auditing procedures and use energy analysis software that meets CEC requirements.</p>
  <div class="bar-black">The HERS Rater will inspect and assess all the major energy efficiency features of your home:</div>

  <ul class="checklist checklist-a">
    <li>Air leaks</li>
    <li>Cooling system</li>
    <li>Heating system</li>
    <li>Cooling/heating duct system</li>
    <li>Water heating system</li>
    <li>Insulation (attic, walls, floor, roof)</li>
  </ul>
  <ul class="checklist checklist-b">
    <li>Windows</li>
    <li>Lighting</li>
    <li>Major appliances</li>
    <li>Solar (if any)</li>
    <li>Other energy uses</li>
    <li>Prior energy bills</li>
  </ul>

  <div class="notes">
    <p>*Thermlio Energy Ratings includes a free duct leakage test and free building envelope leakage test with each home energy audit.</p>
    <p>Heating and cooling ducts in an average California home leak almost 30 percent. That is why when heating or cooling equipment is replaced, testing the system's ducts for leaks is now required by building officials in many parts of the state.</p>
    <p>*You wouldn't buy a new car without knowing the "miles per gallon", so why buy a home without knowing the "home energy rating?"</p>
    <p>*After your mortgage payment, your energy bill is often the second largest monthly home ownership expense.</p>
    <p>*Combine an Energy Efficient Mortgage (EEM) with other programs and you may be able to borrow up to $40,000 or more for efficiency improvements. Ask a knowledgeable lender if an EEM is right for you.</p>
  </div>
</main>
</body>
</html>
```